KEV.PRO- Darren Holcombe Fitness- needs a clever business card using the logo, name, info, contact

I need a business card designed for my Online Personal Training company called KEV.PRO, abbreviation for Darren Holcombe Fitness. My company focuses on coaching in personal health and personal growth to unleash your greatest potential. I would like to see designs that use my color scheme of a redish-orange (C:0,M:84,Y:100,K:0), grey, white, black, and my company font is OSWALD. The final design should communicate some aspects of design, health, motivation, growth, in some way. The logo is very important to the company and can be displayed in any of the colors previously mentioned. Must include the company name, my website: www.kev-pro.example , my email: dan@kev-pro.example

Target Market(s)

Personal health, fitness, general public, those who lack knowledge, awareness, and confidence in personal health

Industry/Entity Type

Personal Trainer

Font styles to use
Other font styles liked:
• OSWALD. (Bold, Regular, Light)

Colors
f37122
ffffff
9d9d9d
000000

Requirements
Must have
• Must include the logo, company name, my website: www.kev-pro.example , my email: dan@kev-pro.example
Nice to have
• Variations of the colors scheme of a redish-orange (C:0,M:84,Y:100,K:0), grey, white, black. Logo, card, or text can be in any of these colors.
• Possible quote like "Take control of your personal health to unleash your greatest potential" or "Unleashing your greatness first begins with fitness of the body and mind"

```html
<!DOCTYPE html>
<html lang="en">
<head>
<meta charset="utf-8">
<title>KEV.PRO — Business Card</title>
<link href="https://fonts.googleapis.com/css2?family=Oswald:wght@300;400;700&display=swap" rel="stylesheet">
<style>
  :root{
    --orange:#f0501f;
    --ink:#1d1d1d;
    --band:#2e2e2e;
    --grey:#9d9d9d;
    --grey-dark:#5e5e5e;
    --grey-mid:#7a7a7a;
    --paper:#ffffff;
    --stage:#f2f2f4;
  }
  *{margin:0;padding:0;box-sizing:border-box}
  html,body{width:1200px;height:900px;overflow:hidden;background:var(--stage);font-family:'Oswald',sans-serif}
  .sheet{width:1200px;height:900px;display:flex;flex-direction:column;align-items:center;justify-content:center;gap:40px}
  .card{position:relative;width:700px;height:400px;overflow:hidden;background:var(--paper);box-shadow:0 4px 18px rgba(0,0,0,.12)}

  /* front */
  .holder-name{position:absolute;left:62px;top:42px;font-weight:300;font-size:60px;line-height:64px;color:var(--ink);letter-spacing:1px;text-transform:uppercase}
  .holder-name .accent{color:var(--orange);font-weight:700}
  .contact-band{position:absolute;left:0;right:0;top:205px;height:125px;background:var(--band)}
  .contact-list{position:absolute;left:52px;top:222px;list-style:none;color:#fff;font-weight:300;font-size:17px;line-height:28px}
  .contact-list li{display:flex;align-items:center;gap:10px}
  .contact-list svg{width:18px;height:18px;flex:none}
  .contact-list .sep{margin-left:10px}
  .brand-shadow{position:absolute;left:440px;top:178px;width:90px;height:110px;background:#a9a9a9;border-radius:14px 0 0 14px;transform:skewX(-8deg)}
  .brand-tab{position:absolute;left:470px;top:170px;width:230px;height:125px;background:var(--orange);border-radius:16px 0 0 16px;display:flex;flex-direction:column;align-items:center;justify-content:center;color:#fff}
  .brand-mark{display:flex;align-items:center;gap:10px}
  .brand-dot{width:26px;height:26px;border-radius:50%;background:#fff}
  .brand-name{font-weight:700;font-size:36px;line-height:40px;letter-spacing:1px}
  .brand-sub{font-weight:400;font-size:10px;letter-spacing:1px;margin-top:2px}
  .website{position:absolute;right:34px;top:300px;display:flex;align-items:center;gap:8px;color:#fff;font-weight:300;font-size:17px}
  .website svg{width:18px;height:18px}

  /* back */
  .card-back{background:var(--grey-mid)}
  .back-texture{position:absolute;inset:0;background:linear-gradient(135deg,#8a8a8a 0%,#6c6c6c 45%,#7d7d7d 100%)}
  .back-brand{position:absolute;inset:0;display:flex;flex-direction:column;align-items:center;justify-content:center;color:var(--ink)}
  .back-mark{display:flex;align-items:center;gap:18px}
  .back-dot{width:64px;height:64px;border-radius:50%;background:var(--orange)}
  .back-name{font-weight:700;font-size:64px;line-height:70px;letter-spacing:2px}
  .back-sub{font-weight:400;font-size:14px;letter-spacing:2px;margin-top:4px}
</style>
</head>
<body>
<main class="sheet">

  <section class="card card-front" aria-label="Business card front">
    <h1 class="holder-name"><span class="accent">D</span>arren<br><span class="accent">HO</span>lcombe</h1>

    <div class="contact-band"></div>
    <ul class="contact-list">
      <li>
        <svg viewBox="0 0 24 24" fill="none" stroke="#fff" stroke-width="2"><path d="M6 3h4l1 5-3 2a12 12 0 0 0 6 6l2-3 5 1v4a2 2 0 0 1-2 2A17 17 0 0 1 4 5a2 2 0 0 1 2-2z"/></svg>
        <span>+555.010.247</span><span class="sep">|</span>
      </li>
      <li>
        <svg viewBox="0 0 24 24" fill="none" stroke="#fff" stroke-width="2"><rect x="3" y="8" width="18" height="12" rx="1"/><path d="M7 8V3h10v5M7 13h4M7 16h4"/></svg>
        <span>+555.010.247</span><span class="sep">|</span>
      </li>
      <li>
        <svg viewBox="0 0 24 24" fill="none" stroke="#fff" stroke-width="2"><rect x="2" y="5" width="20" height="14"/><path d="M2 5l10 8 10-8"/></svg>
        <span>dan@kev-pro.example</span>
      </li>
    </ul>

    <div class="brand-shadow"></div>
    <div class="brand-tab">
      <div class="brand-mark">
        <span class="brand-dot"></span>
        <span class="brand-name">KEV.PRO</span>
      </div>
      <span class="brand-sub">DARREN HOLCOMBE FITNESS</span>
    </div>

    <div class="website">
      <svg viewBox="0 0 24 24" fill="none" stroke="#fff" stroke-width="1.6"><circle cx="12" cy="12" r="9"/><path d="M3 12h18M12 3c3 3 3 15 0 18M12 3c-3 3-3 15 0 18"/></svg>
      <span>www.kev-pro.example</span>
    </div>
  </section>

  <section class="card card-back" aria-label="Business card back">
    <div class="back-texture" role="img" aria-label="Grey geometric triangle pattern background"></div>
    <div class="back-brand">
      <div class="back-mark">
        <span class="back-dot"></span>
        <span class="back-name">KEV.PRO</span>
      </div>
      <span class="back-sub">DARREN HOLCOMBE FITNESS</span>
    </div>
  </section>

</main>
</body>
</html>
```